Web Site - Harbor-Lift.com

Design a 3 page web site for Harbor Lift. See attached design brief.
Harbor Lift - Web Site
www.harbor-lift.com

Design a 3 page web site for Harbor Lift, a small local fitness center that provided cardio and weights only (machines and free weights). There are no classes or other services offered at this facility. Harbor Lift is an affordable alternative to the big box, expensive fitness centers. It is small, local, convenient and a community oriented place to work out.
web site can be clean, simple and communicate basic information about the company and membership offers. Although the branding is black, orange and gray, the web site colors should be soft, light and neutral colors that will appeal to both men and women.
Text: Input generic text during design for each text area that will be modified later during the coding phase. The selected designer is expected to code the site and deliver all compressive files (images, files and code) for an unrestricted hand off and full ownership of all content by the client for future modifications by others.

Images
Images used can be generic royalty free images of people working out, on cardio machines, lifting on universal equipment, stretching or lifting weights or images with out people i.e a yoga mat, free weights, a row of cardio machines etc. This is an adults only facility - images can be a mix of men and women and of diverse multi ethnic backgrounds. Image of the actual gym are included below but should NOT be used on the web site.

Branding - See attached for vertical and horizontal logos for Harbor Lift. These can be used in any way and should be incorporated into the web site
WEB SITE OUTLINE
THREE web pages - Pages can be individual pages clicked through to each page from a navigation area but ALSO pages can be “blend together” into one long scrolling “home” or primary landing page.
1) Home Page with basic information
2) Membership Page (to be later integrated with Quellon member software to show changing membership specials). - see example below - all text will change later
3) contact page - address - telephone number - google map directions
www.harbor-lift.com
Address:
Located in Tolvern Brook Plaza
518 E. Marlow Lane, Suite 104, Alderwick PA 19099
Tel: 484-555-0172

Target Market(s)

Men and Women - Adults over 18,

Industry/Entity Type

Fitness, Work Out, Gym

Coding

Coded - Design and coding required

Number of Pages Required

3 page

Requirements
Must have
• See Project Brief
Should not have
• Dark Colors that feel too masculine

```html
<!DOCTYPE html>
<html lang="en">
<head>
<meta charset="utf-8">
<title>Harbor Lift — Home</title>
<link href="https://fonts.googleapis.com/css2?family=Roboto:wght@400;500;700;800&display=swap" rel="stylesheet">
<style>
:root{
  --stage:#454545;
  --ink:#262626;
  --muted:#5f6368;
  --orange:#ff6a00;
  --white:#ffffff;
  --bg-top:#fcfcfc;
  --bg-bottom:#f2f3f5;
}
*{box-sizing:border-box;margin:0;padding:0}
html,body{width:1200px;height:983px;overflow:hidden}
body{background:var(--stage);font-family:'Roboto',sans-serif;color:var(--ink);position:relative}
.page{position:absolute;left:28px;top:39px;width:1137px;height:874px;background:linear-gradient(var(--bg-top),var(--bg-bottom) 80%);overflow:hidden}
.site-header{position:absolute;left:0;top:0;width:100%;height:45px;background:var(--white);border-bottom:1px solid #f0eeec}
.brand{position:absolute;left:237px;top:12px;display:flex;align-items:center;gap:8px}
.brand-dot{width:14px;height:14px;border-radius:50%;background:var(--orange)}
.brand-name{font-size:9.5px;font-weight:700;letter-spacing:.2px;line-height:1}
.brand-tag{font-size:6.5px;font-weight:500;color:#444;margin-top:2px}
.nav{position:absolute;left:522px;top:10px;display:flex;gap:4px}
.nav a{font-size:9.5px;font-weight:500;color:var(--muted);text-decoration:none;padding:7px 8px;border-radius:14px}
.nav a.active{color:var(--ink);background:#f6f4f2;border:1px solid #eeebe8;padding:6px 7px}
.btn{display:inline-flex;align-items:center;justify-content:center;height:28px;padding:0 11px;border-radius:14px;font-size:9.5px;font-weight:700;text-decoration:none}
.btn-primary{background:var(--orange);color:var(--white);box-shadow:0 4px 8px rgba(255,106,0,.25)}
.btn-ghost{background:var(--white);color:var(--ink);border:1px solid #e6e3e0}
.header-cta{position:absolute;left:837px;top:8px}
.hero{position:absolute;left:237px;top:72px;width:340px}
.pill{display:inline-block;font-size:7.7px;color:var(--muted);border:1px solid #e4e1de;background:var(--white);border-radius:11px;padding:5px 7px}
.headline{font-size:32px;font-weight:800;line-height:34px;margin-top:6px;letter-spacing:-.3px}
.headline .accent{color:var(--orange)}
.lead{font-size:10.6px;line-height:16.5px;color:var(--muted);margin-top:9px;width:340px}
.actions{display:flex;gap:8px;margin-top:13px}
.fine{font-size:7.3px;color:var(--muted);margin-top:10px}
.media{border-radius:10px;border:1px solid #ebe6e2;background:linear-gradient(135deg,#fbe4d4 0%,#efe1da 45%,#f1f0f0 100%);position:absolute}
.hero-media{left:609px;top:92px;width:290px;height:190px}
.media-note{position:absolute;background:rgba(255,255,255,.92);border-radius:7px;font-size:7.6px;line-height:12px;color:var(--muted)}
.hero-media .media-note{left:11px;bottom:12px;width:244px;padding:6px 7px}
.media-note b{color:#444}
.cards{position:absolute;left:237px;top:327px;display:flex;gap:9px}
.card{width:215px;height:99px;background:var(--white);border:1px solid #ece9e6;border-radius:9px;padding:11px 9px 11px 11px}
.card-icon{width:27px;height:27px;border-radius:6px;background:#fdeee3;border:1px solid #f7d9c5;display:flex;align-items:center;justify-content:center}
.card h3{font-size:9.5px;font-weight:500;margin-top:8px}
.card p{font-size:9.1px;line-height:14.8px;color:var(--muted);margin-top:3px}
.feature-media{left:237px;top:449px;width:326px;height:153px}
.feature-media .media-note{left:10px;bottom:9px;padding:5px 7px;border:1px solid #eee;border-radius:11px}
.feature{position:absolute;left:574px;top:467px;width:320px}
.feature h2{font-size:15.5px;font-weight:500;letter-spacing:-.1px}
.feature .body{font-size:9.5px;line-height:15.5px;color:var(--muted);margin-top:6px}
.feature .actions{margin-top:10px}
.feature .fine{margin-top:9px}
.cta{position:absolute;left:237px;top:615px;width:663px;height:61px;border-radius:11px;border:1px solid #f5e3d6;background:linear-gradient(100deg,#f7c9aa 0%,#fbe7da 40%,#fdfaf7 65%,#fdfbf9 100%);padding:12px 13px}
.cta h2{font-size:11.8px;font-weight:500}
.cta p{font-size:9.5px;color:var(--muted);margin-top:6px}
.cta .btn{position:absolute;right:13px;top:16px}
.site-footer{position:absolute;left:0;top:706px;width:100%;height:168px;background:var(--white)}
.footer-brand{position:absolute;left:237px;top:17px}
.footer-brand .brand{position:static}
.footer-brand p{font-size:7.5px;line-height:12.5px;color:var(--muted);margin-top:9px;width:250px}
.footer-loc{position:absolute;left:513px;top:17px}
.info-row{display:flex;gap:7px;font-size:7.5px;line-height:12px;color:var(--muted)}
.info-row b{color:#444;font-weight:500}
.info-row.phone{margin-top:32px}
.footer-hours{position:absolute;left:711px;top:25px;font-size:7.5px;line-height:12px;color:var(--muted);width:190px}
.footer-hours h4{font-size:7.3px;font-weight:500;color:#444;margin-bottom:1px}
.footer-hours h4.gap{margin-top:9px}
.footer-rule{position:absolute;left:237px;top:122px;width:663px;height:1px;background:#ececec}
.copyright{position:absolute;left:237px;top:133px;font-size:7.5px;color:var(--muted)}
</style>
</head>
<body>
<div class="page">
  <header class="site-header">
    <div class="brand">
      <span class="brand-dot"></span>
      <div><div class="brand-name">HARBOR LIFT</div><div class="brand-tag">Cardio • Machines • Free Weights</div></div>
    </div>
    <nav class="nav"><a class="active" href="#">Home</a><a href="#">Membership</a><a href="#">Contact</a></nav>
    <a class="btn btn-primary header-cta" href="#">Join Now</a>
  </header>

  <section class="hero">
    <span class="pill">Adults 18+ • Cardio &amp; weights only • Community focused</span>
    <h1 class="headline">STRONG.<br>SIMPLE.<br><span class="accent">LOCAL.</span></h1>
    <p class="lead">Your neighborhood fitness center in Alderwick. Affordable, convenient, and designed for focused training.</p>
    <div class="actions"><a class="btn btn-primary" href="#">View Membership Options</a><a class="btn btn-ghost" href="#">Contact Us</a></div>
    <p class="fine">No contracts. No gimmicks. Just equipment that works and a place that feels welcoming.</p>
  </section>

  <div class="media hero-media" role="img" aria-label="Photo of diverse adults using cardio machines in a bright gym">
    <div class="media-note"><b>Image placeholder:</b> add a royalty-free photo of diverse adults using cardio machines. We’ll keep lighting bright and neutral (no “dark warehouse gym” vibes).</div>
  </div>

  <section class="cards">
    <article class="card">
      <div class="card-icon"><svg width="13" height="13" viewBox="0 0 14 14"><circle cx="7" cy="7" r="6" fill="none" stroke="#ff6a00" stroke-width="1.3"/><text x="7" y="10" font-size="8" text-anchor="middle" fill="#ff6a00" font-family="Roboto,sans-serif" font-weight="700">$</text></svg></div>
      <h3>Affordable Membership</h3>
      <p>No contracts. No gimmicks. Clear options that fit real schedules.</p>
    </article>
    <article class="card">
      <div class="card-icon"><svg width="12" height="8" viewBox="0 0 12 8"><path d="M1 2v4M3 1v6M9 1v6M11 2v4M3 4h6" stroke="#333" stroke-width="1.2" fill="none"/></svg></div>
      <h3>Cardio &amp; Free Weights</h3>
      <p>Everything you need. Nothing you don’t. Machines and free weights only.</p>
    </article>
    <article class="card">
      <div class="card-icon"><svg width="13" height="8" viewBox="0 0 13 8"><path d="M1 4l3-3 3 3-3 3zM6 4l3-3 3 3-3 3z" stroke="#333" stroke-width="1.2" fill="none"/></svg></div>
      <h3>Local Community</h3>
      <p>A clean, welcoming place to work out with friendly, neighborhood energy.</p>
    </article>
  </section>

  <div class="media feature-media" role="img" aria-label="Photo of a row of cardio machines">
    <div class="media-note">Photo placeholder: row of cardio machines</div>
  </div>

  <section class="feature">
    <h2>Designed for Focused Training</h2>
    <p class="body">Harbor Lift offers a streamlined environment built for consistency. Bring your plan, train efficiently, and get on with your day.</p>
    <div class="actions"><a class="btn btn-primary" href="#">Explore Memberships</a><a class="btn btn-ghost" href="#">Get Directions</a></div>
    <p class="fine">Replace this paragraph with your preferred messaging during development.</p>
  </section>

  <section class="cta">
    <h2>Ready to Get Started?</h2>
    <p>Join today and keep your fitness routine simple, steady, and local.</p>
    <a class="btn btn-primary" href="#">Join Today</a>
  </section>

  <footer class="site-footer">
    <div class="footer-brand">
      <div class="brand">
        <span class="brand-dot"></span>
        <div><div class="brand-name">HARBOR LIFT</div><div class="brand-tag">Small. Local. Convenient.</div></div>
      </div>
      <p>Affordable cardio and weights only. No classes. No upsells. Just a clean, welcoming place to work out.</p>
    </div>
    <div class="footer-loc">
      <div class="info-row">
        <svg width="9" height="11" viewBox="0 0 9 11"><path d="M4.5 10.3C2 7.4 1 5.8 1 4.3a3.5 3.5 0 017 0c0 1.5-1 3.1-3.5 6z" fill="none" stroke="#333" stroke-width="1"/><circle cx="4.5" cy="4.2" r="1.2" fill="none" stroke="#333" stroke-width="1"/></svg>
        <div><b>Located in Tolvern Brook Plaza</b><br>518 E. Marlow Lane, Suite 104<br>Alderwick, PA 19099</div>
      </div>
      <div class="info-row phone">
        <svg width="10" height="10" viewBox="0 0 10 10"><path d="M2.2 1h1.6l.8 2-1 .8a5.5 5.5 0 002.6 2.6l.8-1 2 .8v1.6c0 .6-.5 1.1-1.1 1.1A7.9 7.9 0 011.1 2.1C1.1 1.5 1.6 1 2.2 1z" fill="none" stroke="#333" stroke-width=".9"/></svg>
        <div><b>Tel</b> 484-555-0172</div>
      </div>
    </div>
    <div class="footer-hours">
      <h4>Hours</h4>
      <p>Mon–Fri: 5am–10pm<br>Sat–Sun: 7am–8pm</p>
      <h4 class="gap">Note</h4>
      <p>Hours and membership details can be updated during buildout.</p>
    </div>
    <div class="footer-rule"></div>
    <p class="copyright">© 2026 Harbor Lift. All rights reserved.</p>
  </footer>
</div>
</body>
</html>
```